tidal box

TIDAL BOX mobile technology servicesPhone and tablet repairs, screens data recovery.

Industry/Entity Type

Data Recovery

Contact Information for Business Card

0491 573 086

Colors
33a6d7
f04a50
0a90cc
e34197

Requirements
Must have
• Liam hardy
Nice to have
• White background

```html
<!DOCTYPE html>
<html lang="en">
<head>
<meta charset="utf-8">
<title>tidal box — business card</title>
<link rel="stylesheet" href="https://fonts.googleapis.com/css2?family=Poppins:wght@400;500;600&family=Josefin+Sans:wght@600;700&display=swap">
<style>
  :root {
    --brand-blue: #33a6d7;
    --deep-blue: #0a90cc;
    --brand-red: #f04a50;
    --accent-pink: #e34197;
    --card-bg: #f4f4f4;
    --page-bg: #ffffff;
  }
  * { margin: 0; padding: 0; box-sizing: border-box; }
  html, body {
    width: 1200px;
    height: 742px;
    overflow: hidden;
    background: var(--page-bg);
  }
  .card {
    position: relative;
    width: 1200px;
    height: 742px;
    padding: 22px;
  }
  .card-face {
    position: relative;
    width: 100%;
    height: 100%;
    background: var(--card-bg);
  }
  .phone-number {
    position: absolute;
    left: 55px;
    top: 62px;
    font-family: "Poppins", sans-serif;
    font-weight: 500;
    font-size: 58px;
    line-height: 1;
    letter-spacing: 2px;
    color: var(--brand-red);
    white-space: nowrap;
  }
  .contact-person {
    position: absolute;
    left: 838px;
    top: 52px;
    width: 280px;
    text-align: center;
    font-family: "Josefin Sans", sans-serif;
    font-variant: small-caps;
    line-height: 1;
  }
  .contact-name {
    display: block;
    font-size: 72px;
    font-weight: 600;
    letter-spacing: 2px;
    color: var(--brand-blue);
  }
  .contact-surname {
    display: block;
    margin-top: 4px;
    font-size: 44px;
    font-weight: 700;
    letter-spacing: 1px;
    color: var(--brand-red);
  }
  .device-illustration {
    position: absolute;
    left: 390px;
    top: 76px;
    width: 490px;
    height: 268px;
  }
  .brand-name {
    position: absolute;
    left: 0;
    right: 0;
    top: 352px;
    text-align: center;
    font-family: "Poppins", sans-serif;
    font-weight: 600;
    font-size: 150px;
    line-height: 1;
    letter-spacing: 10px;
    color: var(--brand-red);
  }
  .tagline {
    position: absolute;
    left: 0;
    right: 0;
    text-align: center;
    font-family: "Josefin Sans", sans-serif;
    font-weight: 700;
    font-size: 38px;
    line-height: 1;
    text-transform: uppercase;
    letter-spacing: 3px;
    color: var(--brand-blue);
    white-space: nowrap;
  }
  .tagline-services { top: 540px; }
  .tagline-repairs { top: 604px; }
</style>
</head>
<body>
  <main class="card">
    <section class="card-face">
      <p class="phone-number">0491 573 086</p>

      <p class="contact-person">
        <span class="contact-name">Liam</span>
        <span class="contact-surname">Hardy</span>
      </p>

      <svg class="device-illustration" viewBox="0 0 490 268" role="img" aria-label="Illustration of a cracked smartphone and tablet">
        <defs>
          <linearGradient id="device-tone" x1="0" y1="0" x2="1" y2="1">
            <stop offset="0" stop-color="#33a6d7"/>
            <stop offset="1" stop-color="#f04a50"/>
          </linearGradient>
        </defs>
        <rect x="172" y="4" width="314" height="258" rx="16" fill="url(#device-tone)" opacity="0.55"/>
        <rect x="4" y="94" width="168" height="170" rx="16" fill="url(#device-tone)" opacity="0.55"/>
      </svg>

      <h1 class="brand-name">tidal box</h1>

      <p class="tagline tagline-services">Mobile technology services</p>
      <p class="tagline tagline-repairs">Phone &amp; tablet repairs, data recovery.</p>
    </section>
  </main>
</body>
</html>
```